business card with 2 locations on 1 card

I need a modern looking business card that I would use at 2 different locations. Possibly 1 location on 1 side and other location on other side. One should be able to distinguish the 2 locations immediately before having to read the address or description on card. You can take a look at my website to see what I'm drawn to. The logo is brand new that I just purchased on Pixel Harbor. I want to emphasize family.
Updates

Let's not use the yellow and blue colors. Added Thursday, August 31, 2017

Target Market(s)

women and children

Industry/Entity Type

Health And Wellness

Contact Information for Business Card

Business name: Willow Nest Chiropractic & Acupuncture
My name: Delsa Brook
Job title: DC, MAOM, LAc (CA), CNS

Location 1
Address: 4817 Marlowe Blvd, Suite C-200, Frisco, TX 75036
Phone: (469) 555-0182
Fax: (972) 555-0147

Location 2
Address: 1786 Tenley Road, Suite 300, Plano, TX 75079
Phone: (469) 555-0195
Fax: (972) 555-0147

Email: drdelsabrook@mailvex.example
Website: www.drdelsabrook.example

Font styles to use
Serif
Sans Serif

Colors

Designer to choose colors to be used in the design.

Requirements
Must have
• distinction between 2 locations.
Nice to have
• Colors preference below is there. But I like to see what you come up with too!

```html
<!DOCTYPE html>
<html lang="en">
<head>
<meta charset="utf-8">
<title>Willow Nest Chiropractic &amp; Acupuncture — Business Card</title>
<link rel="stylesheet" href="https://fonts.googleapis.com/css2?family=Lato:wght@300;400;700;900&display=swap">
<style>
  :root {
    --page-bg: #e9e8e4;
    --card-bg: #f7f8f8;
    --ink: #3f4a4b;
    --ink-soft: #5d6767;
    --rule: #8d9595;
    --rule-light: #b4baba;
    --leaf: #6f9a3d;
  }
  * { box-sizing: border-box; margin: 0; padding: 0; }
  html, body {
    width: 1200px; height: 800px; overflow: hidden;
    background: var(--page-bg);
    font-family: "Lato", sans-serif;
    color: var(--ink);
  }
  .canvas { position: relative; width: 1200px; height: 800px; }

  .card {
    position: absolute; left: 285px; width: 630px; height: 360px;
    background: var(--card-bg);
    box-shadow: 0 2px 10px rgba(0,0,0,.12);
  }
  .card--front { top: 25px; }
  .card--back { top: 415px; }

  /* Front */
  .front-frame {
    position: absolute; left: 38px; top: 38px; right: 38px; bottom: 38px;
    border: 1px solid var(--rule);
  }
  .brand {
    position: absolute; left: 40px; top: 50%; transform: translateY(-50%);
    display: flex; align-items: center; gap: 12px;
  }
  .brand-mark {
    width: 48px; height: 48px; border-radius: 50%;
    border: 2px solid var(--ink); background: var(--card-bg);
  }
  .brand-name {
    font-weight: 700; font-size: 15px; line-height: 1.25;
    letter-spacing: .5px; color: var(--ink); width: 160px;
  }
  .front-divider {
    position: absolute; left: 282px; top: 38px; width: 1px; height: 54px;
    background: var(--rule);
  }
  .person { position: absolute; left: 310px; top: 38px; }
  .person-name { font-weight: 900; font-size: 24px; color: var(--ink); }
  .person-title { font-weight: 400; font-size: 14px; color: var(--ink-soft); margin-top: 2px; }
  .contact {
    position: absolute; left: 310px; top: 154px;
    font-weight: 300; font-size: 15px; line-height: 1.6; color: var(--ink);
  }

  /* Back */
  .location { position: absolute; width: 262px; }
  .location--one { left: 40px; top: 110px; }
  .location--two { left: 318px; top: 28px; }
  .location-head {
    height: 90px; border: 1px solid var(--rule);
    display: flex; align-items: center; justify-content: center;
    font-weight: 900; font-size: 20px; letter-spacing: .5px; color: var(--ink);
  }
  .info-row {
    height: 36px; margin-top: 8px; border: 1px solid var(--rule);
    display: flex; align-items: center;
  }
  .info-icon { width: 36px; display: flex; justify-content: center; }
  .info-icon svg { width: 14px; height: 14px; fill: var(--ink); }
  .info-tick { width: 1px; height: 18px; background: var(--rule-light); margin-right: 10px; }
  .info-text { font-size: 12px; color: var(--ink); white-space: nowrap; }
  .info-text--small { font-size: 9px; }
</style>
</head>
<body>
<div class="canvas">

  <section class="card card--front" aria-label="Card front">
    <div class="front-frame">
      <div class="brand">
        <div class="brand-mark"></div>
        <div class="brand-name">Willow Nest Chiropractic &amp; Acupuncture</div>
      </div>
      <div class="front-divider"></div>
      <div class="person">
        <div class="person-name">Delsa Brook</div>
        <div class="person-title">DC, MAOM, LAc (CA), CNS</div>
      </div>
      <div class="contact">
        <div>www.drdelsabrook.example</div>
        <div>drdelsabrook@mailvex.example</div>
      </div>
    </div>
  </section>

  <section class="card card--back" aria-label="Card back">
    <div class="location location--one">
      <div class="location-head">LOCATION 1</div>
      <div class="info-row">
        <span class="info-icon"><svg viewBox="0 0 14 14"><path d="M7 0a5 5 0 0 0-5 5c0 3.6 5 9 5 9s5-5.4 5-9a5 5 0 0 0-5-5zm0 7a2 2 0 1 1 0-4 2 2 0 0 1 0 4z"/></svg></span>
        <span class="info-tick"></span>
        <span class="info-text info-text--small">4817 Marlowe Blvd, Suite C-200, Frisco, TX 75036</span>
      </div>
      <div class="info-row">
        <span class="info-icon"><svg viewBox="0 0 14 14"><path d="M3 0h8a1 1 0 0 1 1 1v12a1 1 0 0 1-1 1H3a1 1 0 0 1-1-1V1a1 1 0 0 1 1-1zm.5 1.5v10h7v-10z"/></svg></span>
        <span class="info-tick"></span>
        <span class="info-text">(469) 555-0182</span>
      </div>
      <div class="info-row">
        <span class="info-icon"><svg viewBox="0 0 14 14"><path d="M3 0h8v4H3zM1 5h12v7h-2v2H3v-2H1zm3 5v3h6v-3z"/></svg></span>
        <span class="info-tick"></span>
        <span class="info-text">(972) 555-0147 (FAX)</span>
      </div>
    </div>

    <div class="location location--two">
      <div class="location-head">LOCATION 2</div>
      <div class="info-row">
        <span class="info-icon"><svg viewBox="0 0 14 14"><path d="M7 0a5 5 0 0 0-5 5c0 3.6 5 9 5 9s5-5.4 5-9a5 5 0 0 0-5-5zm0 7a2 2 0 1 1 0-4 2 2 0 0 1 0 4z"/></svg></span>
        <span class="info-tick"></span>
        <span class="info-text info-text--small">1786 Tenley Road, Suite 300, Plano, TX 75079</span>
      </div>
      <div class="info-row">
        <span class="info-icon"><svg viewBox="0 0 14 14"><path d="M3 0h8a1 1 0 0 1 1 1v12a1 1 0 0 1-1 1H3a1 1 0 0 1-1-1V1a1 1 0 0 1 1-1zm.5 1.5v10h7v-10z"/></svg></span>
        <span class="info-tick"></span>
        <span class="info-text">(469) 555-0195</span>
      </div>
      <div class="info-row">
        <span class="info-icon"><svg viewBox="0 0 14 14"><path d="M3 0h8v4H3zM1 5h12v7h-2v2H3v-2H1zm3 5v3h6v-3z"/></svg></span>
        <span class="info-tick"></span>
        <span class="info-text">(972) 555-0147 (FAX)</span>
      </div>
    </div>
  </section>

</div>
</body>
</html>
```